Backbone Bright Practice Hour

I need a podcast artwork designed for me for a new podcast I am launching
Target Market(s)
Chiropractors
Industry/Entity Type
Chiropractor
Requirements
Must have
- This image and the title of the show

```html
<!DOCTYPE html>
<html lang="en">
<head>
<meta charset="utf-8">
<title>Backbone Bright Practice Hour</title>
<link rel="stylesheet" href="https://fonts.googleapis.com/css2?family=Bebas+Neue&display=swap">
<style>
  :root {
    --teal-deep: #17a08f;
    --teal-mid: #4dbaa0;
    --sage: #a8d3b5;
    --sand: #efe5c2;
    --cream: #fbf6d6;
    --title-ink: #fdfbd6;
    --host-light: #c9d8cf;
    --host-dark: #2f3a22;
    --shadow-teal: #1a9c8a;
  }
  html, body {
    margin: 0;
    padding: 0;
    width: 1200px;
    height: 1200px;
    overflow: hidden;
  }
  .cover {
    position: relative;
    width: 1200px;
    height: 1200px;
    overflow: hidden;
    background: linear-gradient(
      to bottom,
      var(--teal-deep) 0%,
      var(--teal-mid) 25%,
      var(--sage) 42%,
      var(--sand) 62%,
      var(--cream) 100%
    );
  }
  .show-title {
    position: absolute;
    inset: 0;
    width: 1200px;
    height: 1200px;
  }
  .show-title text {
    font-family: "Bebas Neue", "Oswald", sans-serif;
    fill: var(--title-ink);
  }
  .title-top { font-size: 160px; }
  .title-main { font-size: 275px; }
  .title-end { font-size: 160px; }
  .host-photo {
    position: absolute;
    left: 120px;
    top: 428px;
    width: 240px;
    height: 772px;
    border-radius: 60px 60px 12px 12px;
    background: linear-gradient(
      to bottom,
      var(--host-light) 0%,
      var(--host-light) 45%,
      var(--host-dark) 55%,
      var(--host-dark) 92%,
      var(--shadow-teal) 100%
    );
  }
</style>
</head>
<body>
  <main class="cover">
    <svg class="show-title" viewBox="0 0 1200 1200" aria-label="Backbone Bright Practice Hour">
      <text class="title-top" x="28" y="132" textLength="1144" lengthAdjust="spacing">BACKBONE BRIGHT</text>
      <text class="title-main" x="28" y="376" textLength="1144" lengthAdjust="spacing">PRACTICE</text>
      <text class="title-end" x="375" y="512" textLength="785" lengthAdjust="spacing">HOUR</text>
    </svg>
    <div class="host-photo" role="img" aria-label="Photo of the host standing in a white shirt, tie and dark trousers, casting a teal shadow"></div>
  </main>
</body>
</html>
```